Product Labels for soaps lines

I have bar soap, liquid soap, lip balm, lotion bar, lotion and bath bomb ,I already have a logo and I need product labels for shape of Square, Circle, Rectangle and oval,

The design need to match my logo.

example of the texts:( rectangle)

Hair Shampoo

100% handmade - Sulfate Free

Ingredients: Canola Oil ,Ricinus Communis (Castor) Seed Oil ,Cocos Nucifera (Coconut) Oil ,Simmondsia Chinensis (Jojoba) Seed Oil ,Aqua ( Water),Potassium hydroxide ,Fragrance

NT WT 8 OZ

Rectangle label measurement : 2 *4 for liquid shampoo
rectangle-horizontal or oval : 2.5*2 for bar soap
Circle : 1.5 for lip balm and 2 ' for lotion bar
rectangle label : 2*3 for lotion
circle label: 2.3 for body butter
rectangle label :1*1.5 facial serum

example of the texts:( medium rectangle)

Natural Body Soap

Ricinus Communis (Castor) Seed Oil ,Cocos Nucifera (Coconut) Oil ,Hydrogenated Palm Oil ,Prunus Amygdalus Dulcis (Sweet Almond) Oil ,Butyrospermum Parkii (Shea Butter) Fruit ,Beeswax ,Oryza Sativa (Rice) Bran Oil ,Olea Europaea (Olive) Oil ,Aqua ( Water),Sodium hydroxide ,Raw Goat Milk,Mica,Fragrance
Approx. 5 OZ

hand Wash/Body Wash lable size 2*4
Ricinus Communis (Castor) Seed Oil ,Cocos Nucifera (Coconut) Oil ,Theobroma Cacao (Cocoa) Seed Butter ,Olea Europaea (Olive) Oil ,Oryza Sativa (Rice) Bran Oil ,Aqua ( Water),Potassium hydroxide ,Fragrance

Avacado Facial Wash lable size 2*4
Canola Oil ,Ricinus Communis (Castor) Seed Oil ,Cocos Nucifera (Coconut) Oil ,Persea Gratissima (Avocado) Oil ,Prunus Amygdalus Dulcis (Sweet Almond) Oil ,Oryza Sativa (Rice) Bran Oil ,Aqua ( Water),Potassium hydroxide ,Fragrance

Lotion Bar
Cocos Nucifera (Coconut) Oil ,Mangifera Indica (Mango) Seed Butter ,Butyrospermum Parkii (Shea Butter) Fruit ,Beewax

Body Butter
Cocos Nucifera (Coconut) Oil ,Butyrospermum Parkii (Shea Butter) Fruit ,Theobroma Cacao (Cocoa) Seed Butter ,Helianthus Annuus (Sunflower) Seed Oil

lip balm,
Olea Europaea (Olive) Oil ,Butyrospermum Parkii (Shea Butter) Fruit ,Vitis Vinifera (Grape) Seed Oil ,Beewax,Fragrance

facial serum:1*1.5
Prunus Armeniaca (Apricot) Kernel Oil ,Argania Spinosa (Argan) Nut Oil ,Simmondsia Chinensis (Jojoba) Seed Oil ,Rosa Canina Fruit Oil
Updates

Target Market(s)

Logo color can be changed to a little darker blue

Industry/Entity Type

Hair

Font styles to use
Serif

Colors
fece3e
f04a50
33b7a4
8869ae

Requirements
Must have

• company name " Lather Meadowbrook " is inspired by Tobias on the Moonhill, fun and adventurous spirit, design need to be fun ..
Nice to have
• Fun, Simple and eye catching ..

```html
<!DOCTYPE html>
<html lang="en">
<head>
<meta charset="utf-8">
<title>Body/Hand Wash – Label Variations</title>
<link href="https://fonts.googleapis.com/css2?family=Amarante&family=Kurale&family=Noto+Sans&display=swap" rel="stylesheet">
<style>
  :root {
    --pink-light: #ff88d0;
    --pink-mid: #ee55cc;
    --pink-deep: #e8358f;
    --teal: #1ecfd0;
    --teal-dark: #128c8c;
    --sage: #dcdea0;
    --cream: #eef0d6;
    --bubble: #d6d49c;
    --ink: #3a1408;
    --paper: #ffffff;
    --frame: #333333;
  }
  * { box-sizing: border-box; margin: 0; padding: 0; }
  html, body { width: 1200px; height: 1000px; overflow: hidden; background: var(--paper); }
  .sheet { position: relative; width: 1200px; height: 1000px; font-family: "Noto Sans", sans-serif; }
  .sheet-title { position: absolute; top: 14px; left: 0; width: 1200px; text-align: center; font-size: 30px; font-weight: 400; color: #000; }
  .size-caption { position: absolute; width: 179px; text-align: center; font-size: 16px; color: #000; }

  .label { position: absolute; width: 179px; border: 1px solid var(--frame); background: var(--paper); overflow: hidden; }
  .label.tall { height: 449px; }
  .label.short { height: 269px; }
  .label.tone-light { --brand-bg: var(--pink-light); }
  .label.tone-mid { --brand-bg: var(--pink-mid); }
  .label.tone-deep { --brand-bg: var(--pink-deep); }

  .brand-panel { position: relative; background: var(--brand-bg); height: 125px; }
  .label.short .brand-panel { height: 114px; }
  .brand-name { position: absolute; top: 20px; left: 0; width: 100%; text-align: center; font-family: "Amarante", serif; font-size: 25px; line-height: 27px; color: var(--teal); }
  .bubble-row { position: absolute; left: 0; bottom: 0; width: 100%; height: 28px; background: linear-gradient(to bottom, var(--cream), var(--bubble)); }

  .product-band { background: var(--sage); height: 61px; text-align: center; padding-top: 9px; }
  .label.short .product-band { height: 55px; padding-top: 6px; }
  .product-name { font-family: "Amarante", serif; font-weight: 400; font-size: 20px; color: var(--teal-dark); line-height: 24px; }
  .product-claim { font-family: "Kurale", serif; font-size: 11px; color: var(--ink); line-height: 16px; }

  .details { position: relative; padding: 16px 10px 0 14px; font-family: "Kurale", serif; color: var(--ink); }
  .label.tall .details { height: 263px; }
  .label.short .details { height: 100px; padding: 5px 8px 0 10px; }
  .ingredients { font-size: 12px; line-height: 16px; }
  .label.short .ingredients { font-size: 7.2px; line-height: 10px; }
  .net-weight { position: absolute; left: 19px; font-size: 11px; word-spacing: 4px; }
  .label.tall .net-weight { top: 192px; }
  .label.short .net-weight { left: 12px; top: 80px; font-size: 8px; }
  .bubble-cluster { position: absolute; right: 5px; bottom: 5px; height: 42px; width: 166px; background: linear-gradient(to bottom, var(--cream), var(--bubble)); }
  .label.short .bubble-cluster { width: 48px; height: 22px; }

  .swatch { position: absolute; left: 38px; font-size: 13px; line-height: 15px; }
  .swatch p { padding-left: 5px; }
  .swatch-chip { width: 50px; height: 30px; margin-bottom: 5px; }
  .swatch.light { top: 686px; color: var(--pink-light); }
  .swatch.mid { top: 783px; color: var(--pink-mid); }
  .swatch.deep { top: 880px; color: var(--pink-deep); }
  .swatch.light .swatch-chip { background: var(--pink-light); }
  .swatch.mid .swatch-chip { background: var(--pink-mid); }
  .swatch.deep .swatch-chip { background: var(--pink-deep); }
</style>
</head>
<body>
<main class="sheet">
  <h1 class="sheet-title">Body/Hand Wash</h1>

  <p class="size-caption" style="left:41px;top:86px">2'' x 5''</p>
  <p class="size-caption" style="left:281px;top:86px">2'' x 3''</p>
  <p class="size-caption" style="left:752px;top:84px">2'' x 5''</p>
  <p class="size-caption" style="left:991px;top:82px">2'' x 3''</p>
  <p class="size-caption" style="left:283px;top:460px">2'' x 5''</p>
  <p class="size-caption" style="left:523px;top:460px">2'' x 3''</p>

  <article class="label tall tone-light" style="left:41px;top:132px">
    <div class="brand-panel"><p class="brand-name">Lather Meadowbrook</p><div class="bubble-row" role="img" aria-label="Soap bubble illustration"></div></div>
    <div class="product-band"><h2 class="product-name">Body/Hand wash</h2><p class="product-claim">100% Handmade - Sulfate Free</p></div>
    <div class="details">
      <p class="ingredients">Ingredients:<br>Ricinus Communis (Castor) Seed Oil, Cocos Nucifera (Coconut) Oil, Theobroma Cacao (Cocoa) Seed Butter, Olea Europaea (Olive) Oil, Orgza Sativa (Rice) Bran Oil, Aqua (Water),<br>Potassium Hydroxide,<br>Fragrance</p>
      <p class="net-weight">NT WT ? oz</p>
      <div class="bubble-cluster" role="img" aria-label="Soap bubble illustration"></div>
    </div>
  </article>

  <article class="label short tone-light" style="left:281px;top:131px">
    <div class="brand-panel"><p class="brand-name">Lather Meadowbrook</p><div class="bubble-row" role="img" aria-label="Soap bubble illustration"></div></div>
    <div class="product-band"><h2 class="product-name">Body/Hand wash</h2><p class="product-claim">100% Handmade - Sulfate Free</p></div>
    <div class="details">
      <p class="ingredients">Ingredients: Ricinus Communis (Castor) Seed Oil, Cocos Nucifera (Coconut) Oil, Theobroma Cacao (Cocoa) Seed Butter, Olea Europaea (Olive) Oil, Orgza Sativa (Rice) Bran Oil, Aqua (Water), Potassium Hydroxide, Fragrance</p>
      <p class="net-weight">NT WT ? oz</p>
      <div class="bubble-cluster" role="img" aria-label="Soap bubble illustration"></div>
    </div>
  </article>

  <article class="label tall tone-mid" style="left:752px;top:128px">
    <div class="brand-panel"><p class="brand-name">Lather Meadowbrook</p><div class="bubble-row" role="img" aria-label="Soap bubble illustration"></div></div>
    <div class="product-band"><h2 class="product-name">Body/Hand wash</h2><p class="product-claim">100% Handmade - Sulfate Free</p></div>
    <div class="details">
      <p class="ingredients">Ingredients:<br>Ricinus Communis (Castor) Seed Oil, Cocos Nucifera (Coconut) Oil, Theobroma Cacao (Cocoa) Seed Butter, Olea Europaea (Olive) Oil, Orgza Sativa (Rice) Bran Oil, Aqua (Water),<br>Potassium Hydroxide,<br>Fragrance</p>
      <p class="net-weight">NT WT ? oz</p>
      <div class="bubble-cluster" role="img" aria-label="Soap bubble illustration"></div>
    </div>
  </article>

  <article class="label short tone-mid" style="left:991px;top:128px">
    <div class="brand-panel"><p class="brand-name">Lather Meadowbrook</p><div class="bubble-row" role="img" aria-label="Soap bubble illustration"></div></div>
    <div class="product-band"><h2 class="product-name">Body/Hand wash</h2><p class="product-claim">100% Handmade - Sulfate Free</p></div>
    <div class="details">
      <p class="ingredients">Ingredients: Ricinus Communis (Castor) Seed Oil, Cocos Nucifera (Coconut) Oil, Theobroma Cacao (Cocoa) Seed Butter, Olea Europaea (Olive) Oil, Orgza Sativa (Rice) Bran Oil, Aqua (Water), Potassium Hydroxide, Fragrance</p>
      <p class="net-weight">NT WT ? oz</p>
      <div class="bubble-cluster" role="img" aria-label="Soap bubble illustration"></div>
    </div>
  </article>

  <article class="label tall tone-deep" style="left:283px;top:505px">
    <div class="brand-panel"><p class="brand-name">Lather Meadowbrook</p><div class="bubble-row" role="img" aria-label="Soap bubble illustration"></div></div>
    <div class="product-band"><h2 class="product-name">Body/Hand wash</h2><p class="product-claim">100% Handmade - Sulfate Free</p></div>
    <div class="details">
      <p class="ingredients">Ingredients:<br>Ricinus Communis (Castor) Seed Oil, Cocos Nucifera (Coconut) Oil, Theobroma Cacao (Cocoa) Seed Butter, Olea Europaea (Olive) Oil, Orgza Sativa (Rice) Bran Oil, Aqua (Water),<br>Potassium Hydroxide,<br>Fragrance</p>
      <p class="net-weight">NT WT ? oz</p>
      <div class="bubble-cluster" role="img" aria-label="Soap bubble illustration"></div>
    </div>
  </article>

  <article class="label short tone-deep" style="left:523px;top:505px">
    <div class="brand-panel"><p class="brand-name">Lather Meadowbrook</p><div class="bubble-row" role="img" aria-label="Soap bubble illustration"></div></div>
    <div class="product-band"><h2 class="product-name">Body/Hand wash</h2><p class="product-claim">100% Handmade - Sulfate Free</p></div>
    <div class="details">
      <p class="ingredients">Ingredients: Ricinus Communis (Castor) Seed Oil, Cocos Nucifera (Coconut) Oil, Theobroma Cacao (Cocoa) Seed Butter, Olea Europaea (Olive) Oil, Orgza Sativa (Rice) Bran Oil, Aqua (Water), Potassium Hydroxide, Fragrance</p>
      <p class="net-weight">NT WT ? oz</p>
      <div class="bubble-cluster" role="img" aria-label="Soap bubble illustration"></div>
    </div>
  </article>

  <div class="swatch light"><div class="swatch-chip"></div><p>CMYK</p><p>0 46 18 0 100</p></div>
  <div class="swatch mid"><div class="swatch-chip"></div><p>CMYK</p><p>0 62 13 5 100</p></div>
  <div class="swatch deep"><div class="swatch-chip"></div><p>CMYK</p><p>0 77 37 8 100</p></div>
</main>
</body>
</html>
```